Modern Billboard Ad for Criminal Defense Firm

10.5 x 36 We're looking for something to set us apart from the local competition. Looking for sleek and modern. We're a mid-sized firm in a small market city. We want to give the artist room to be creative on this one.
Thanks

Target Market(s)

Adult clients who have been charged with a crime/DWI

Industry/Entity Type

legal

Font styles to use
Serif
Sans Serif

Requirements
Must have
• Needs to have the firm name in large lettering. Law Offices of Marcus T Whitfield. “PLLC” does not have to be included. Phone number of (555) 384-1927 should be included but not the main focus.
Nice to have
• A call to action or something similar. “Don’t go it alone, call today.”, “ Arrested?”

```html
<!DOCTYPE html>
<html lang="en">
<head>
<meta charset="utf-8">
<title>Marcus T Whitfield – Billboard</title>
<link rel="stylesheet" href="https://fonts.googleapis.com/css2?family=Cinzel:wght@500;700&family=Montserrat:wght@600;700&display=swap">
<style>
  :root {
    --ink: #231f20;
    --paper: #ffffff;
    --accent: #f15a29;
    --photo-light: #a9a9a9;
    --photo-dark: #4a4a4a;
  }
  html, body {
    margin: 0;
    padding: 0;
    width: 1200px;
    height: 350px;
    overflow: hidden;
    background: var(--paper);
  }
  .billboard {
    display: block;
    width: 1200px;
    height: 350px;
  }
  .firm-intro {
    font-family: "Cinzel", serif;
    font-weight: 500;
    fill: var(--accent);
  }
  .firm-name {
    font-family: "Cinzel", serif;
    font-weight: 500;
    fill: var(--paper);
  }
  .headline {
    font-family: "Cinzel", serif;
    font-weight: 700;
    fill: var(--accent);
  }
  .tagline {
    font-family: "Montserrat", sans-serif;
    font-weight: 700;
    fill: var(--ink);
  }
  .cta-label {
    font-family: "Montserrat", sans-serif;
    font-weight: 600;
    fill: var(--ink);
  }
  .phone {
    font-family: "Montserrat", sans-serif;
    font-weight: 700;
    fill: var(--paper);
  }
</style>
</head>
<body>
<svg class="billboard" viewBox="0 0 1200 350" xmlns="http://www.w3.org/2000/svg">
  <defs>
    <linearGradient id="portrait-tone" x1="0" y1="0" x2="1" y2="1">
      <stop offset="0" stop-color="var(--photo-light)"/>
      <stop offset="1" stop-color="var(--photo-dark)"/>
    </linearGradient>
  </defs>

  <polygon class="name-band" points="0,0 783,0 648,156 0,156" fill="var(--ink)"/>

  <text class="firm-intro" x="35" y="66" font-size="38" textLength="318" lengthAdjust="spacingAndGlyphs">Law Offices of</text>
  <text class="firm-name" x="33" y="127" font-size="50" textLength="580" lengthAdjust="spacingAndGlyphs">MARCUS T WHITFIELD</text>

  <text class="headline" x="33" y="252" font-size="78" textLength="552" lengthAdjust="spacingAndGlyphs">ARRESTED?</text>
  <text class="tagline" x="111" y="315" font-size="33" textLength="405" lengthAdjust="spacingAndGlyphs">DON’T GO IT ALONE</text>

  <polygon class="attorney-portrait" role="img" aria-label="Black and white portrait of the attorney in a vest and tie, jacket over his shoulder, against a wooden wall"
           points="652,174 768,29 973,29 973,210 858,350 652,350" fill="url(#portrait-tone)"/>

  <polygon class="phone-panel" points="973,128 1200,128 1200,350 858,350 973,210" fill="var(--accent)"/>

  <text class="cta-label" x="999" y="66" font-size="33" textLength="162" lengthAdjust="spacing">CALL</text>
  <text class="cta-label" x="1004" y="112" font-size="33" textLength="156" lengthAdjust="spacingAndGlyphs">TODAY</text>

  <text class="phone" x="996" y="195" font-size="70" textLength="168" lengthAdjust="spacingAndGlyphs">(555)</text>
  <text class="phone" x="996" y="258" font-size="56" textLength="168" lengthAdjust="spacing">384</text>
  <text class="phone" x="996" y="321" font-size="56" textLength="168" lengthAdjust="spacing">1927</text>
</svg>
</body>
</html>
```